I’m looking for a vibrant, eye-catching package design for our new premium cannabis gummies, TALVEN. This is a high-end cannabis edible gummy made with real fruit, vegan ingredients, and powered by a THC nano emulsion — the most effective way to ingest cannabis. The package will be a square-bottom bag with child-resistant zippers (image of bag attached).

What we want from you? We want your version of what the front of the bag should look like.

The following text elements should be included within your vision of the bag

Talven - Premium Cannabis Gummy
10 pieces per bag | 10mg THC per piece | 100mg THC total
Made with real fruit
Vegan (include a vegan symbol)
Flavors: Assorted flavors (Strawberry, Mango, Pineapple, Orange, Blueberry)
Oregon cannabis icon (attached)
Net Weight 250 grams (bottom of bag)

What is needed after you win.
2 other sizes. Same look but will need to rearrange some elements of the bag. The back of the bag will be the same for all sizes. Will be legal text and nutritional info. Larger two sizes has sides, as per the attached bag. All sizes will have a bottom as well. the first size will have 5 versions for flavors. Other 2 sizes will be 1 design with "assorted flavors".

Target Market(s)

Cannabis market in Oregon

Industry/Entity Type

cannabis

Requirements
Must have
• the Marijuana universal icon for being a cannabis product.
Nice to have
• nice images of fruits
Should not have
• graphic, cartoon images that would appeal to minors.

```html
<!DOCTYPE html>
<html lang="en">
<head>
<meta charset="utf-8">
<title>TALVEN Premium Cannabis Gummies – Pouch Fronts</title>
<link rel="stylesheet" href="https://fonts.googleapis.com/css2?family=Montserrat:wght@400;500;600;900&display=swap">
<style>
  :root {
    --bg: #ffffff;
    --strawberry: #fb5166;
    --strawberry-light: #fd7c8e;
    --strawberry-fruit: #d8202e;
    --blueberry: #5b9bef;
    --blueberry-light: #86c4f5;
    --blueberry-fruit: #2c4f9c;
    --night: #1c2244;
    --night-deep: #141a36;
    --glow-pink: #e8677a;
    --glow-violet: #6a4a8c;
    --nebula-teal: #2f7f86;
    --text-light: #ffffff;
    --text-soft: rgba(255,255,255,.85);
    --badge-dark: #1a1a1a;
    --badge-red: #c8242b;
  }
  * { box-sizing: border-box; margin: 0; padding: 0; }
  html, body { width: 1200px; height: 900px; overflow: hidden; background: var(--bg); }
  body { position: relative; font-family: "Montserrat", sans-serif; }

  .pouch {
    position: absolute;
    top: 98px;
    width: 466px;
    height: 734px;
    border-radius: 4px 4px 10px 10px;
    overflow: hidden;
    background: var(--night);
    color: var(--text-light);
  }
  .pouch--strawberry { left: 104px; --accent: var(--strawberry); --accent-light: var(--strawberry-light); --fruit: var(--strawberry-fruit); }
  .pouch--blueberry  { left: 622px; --accent: var(--blueberry);  --accent-light: var(--blueberry-light); --fruit: var(--blueberry-fruit); }

  .pouch-header {
    position: absolute; inset: 0 0 auto 0; height: 131px;
    background: var(--accent);
  }
  .flavor-rule {
    position: absolute; left: 6px; right: 6px; top: 117px;
    height: 1px; background: var(--text-light);
  }
  .flavor-name {
    position: absolute; left: 0; right: 0; top: 101px;
    text-align: center;
    font-size: 9px; font-weight: 500;
    letter-spacing: 18px; text-indent: 18px;
    color: var(--text-light);
  }
  .flavor-fruit {
    position: absolute; top: 94px; left: 50%;
    width: 18px; height: 22px; margin-left: -9px;
    background: var(--fruit);
    border-radius: 50% 50% 50% 50% / 40% 40% 60% 60%;
  }
  .pouch--blueberry .flavor-fruit { width: 30px; margin-left: -15px; border-radius: 50%; }

  .pouch-art {
    position: absolute; left: 0; right: 0; top: 131px; bottom: 0;
    background:
      radial-gradient(ellipse 55% 20% at 10% 30%, rgba(255,230,220,.85), transparent 70%),
      radial-gradient(ellipse 80% 45% at 15% 50%, var(--glow-pink), transparent 75%),
      radial-gradient(ellipse 50% 35% at 80% 30%, var(--nebula-teal), transparent 75%),
      radial-gradient(ellipse 60% 40% at 50% 18%, var(--glow-violet), transparent 80%),
      linear-gradient(180deg, var(--night) 0%, #3a2f5c 40%, var(--night) 75%, var(--night-deep) 100%);
  }

  .brand-title {
    position: absolute; left: 0; right: 0; top: 134px;
    text-align: center;
    font-weight: 900; font-size: 88px; line-height: 1;
    letter-spacing: -6px;
    color: var(--accent-light);
  }
  .brand-tagline {
    position: absolute; left: 0; right: 0; top: 219px;
    text-align: center;
    font-size: 18px; font-weight: 500;
    letter-spacing: 3.2px;
  }

  .fruit-claim {
    position: absolute; left: 40px; top: 572px;
    display: flex; align-items: center; gap: 10px;
  }
  .vegan-mark {
    width: 38px; height: 38px; border-radius: 50%;
    border: 1.5px solid var(--text-light);
    display: flex; align-items: center; justify-content: center;
    font-size: 7px; font-weight: 600; letter-spacing: .8px;
  }
  .fruit-claim-text {
    font-size: 10px; font-weight: 500; letter-spacing: 1.8px; line-height: 1.5;
  }

  .strain-info {
    position: absolute; left: 40px; top: 626px;
  }
  .strain-type {
    font-size: 9px; letter-spacing: 1.6px; font-weight: 500;
    padding-bottom: 2px;
    border-bottom: 1px solid var(--accent);
    width: 70px;
  }
  .dose { display: flex; align-items: center; gap: 3px; margin-top: 1px; }
  .dose-amount { font-size: 21px; font-weight: 500; line-height: 1; }
  .dose-unit { font-size: 8px; letter-spacing: 1.6px; line-height: 1.15; font-weight: 500; }

  .cannabis-badge {
    position: absolute; left: 384px; top: 628px;
    width: 42px; height: 36px; border-radius: 4px;
    background: var(--badge-red);
    border-left: 14px solid var(--badge-dark);
  }

  .pack-facts {
    position: absolute; left: 40px; right: 40px; top: 684px;
    font-size: 8px; font-weight: 500; letter-spacing: .8px;
    color: var(--text-soft);
    white-space: nowrap;
  }
  .net-weight {
    position: absolute; left: 0; right: 0; top: 708px;
    text-align: center;
    font-size: 9px; font-weight: 500; letter-spacing: 2px;
  }
</style>
</head>
<body>

  <section class="pouch pouch--strawberry">
    <div class="pouch-header"></div>
    <div class="flavor-rule"></div>
    <p class="flavor-name">STRAWBERRY</p>
    <div class="flavor-fruit" role="img" aria-label="Strawberry fruit illustration"></div>
    <div class="pouch-art" role="img" aria-label="Space scene with a rocket launching past a glowing planet under a colourful nebula"></div>
    <h1 class="brand-title">TALVEN</h1>
    <p class="brand-tagline">PREMIUM CANNABIS GUMMIES</p>
    <div class="fruit-claim">
      <span class="vegan-mark">VEGAN</span>
      <p class="fruit-claim-text">MADE WITH<br>REAL FRUIT</p>
    </div>
    <div class="strain-info">
      <p class="strain-type">INDICA</p>
      <div class="dose"><span class="dose-amount">10</span><span class="dose-unit">MG THC<br>PER PIECE</span></div>
    </div>
    <div class="cannabis-badge" role="img" aria-label="Universal cannabis product icon"></div>
    <p class="pack-facts">10 PIECES PER BAG | 10MG THC PER PIECE | 100MG THC TOTAL</p>
    <p class="net-weight">NET WT 250 G</p>
  </section>

  <section class="pouch pouch--blueberry">
    <div class="pouch-header"></div>
    <div class="flavor-rule"></div>
    <p class="flavor-name">BLUEBERRY</p>
    <div class="flavor-fruit" role="img" aria-label="Blueberries illustration"></div>
    <div class="pouch-art" role="img" aria-label="Space scene with a rocket launching past a glowing planet under a colourful nebula"></div>
    <h1 class="brand-title">TALVEN</h1>
    <p class="brand-tagline">PREMIUM CANNABIS GUMMIES</p>
    <div class="fruit-claim">
      <span class="vegan-mark">VEGAN</span>
      <p class="fruit-claim-text">MADE WITH<br>REAL FRUIT</p>
    </div>
    <div class="strain-info">
      <p class="strain-type">INDICA</p>
      <div class="dose"><span class="dose-amount">10</span><span class="dose-unit">MG THC<br>PER PIECE</span></div>
    </div>
    <div class="cannabis-badge" role="img" aria-label="Universal cannabis product icon"></div>
    <p class="pack-facts">10 PIECES PER BAG | 10MG THC PER PIECE | 100MG THC TOTAL</p>
    <p class="net-weight">NET WT 250 G</p>
  </section>

</body>
</html>
```